Catalog copying current designs, web designs and copywrite.

I am looking for someone to recreate a draft catalog using the same design process.

My entire brief with the photo samples and icons would not fit in here. They are in the google docs folder as below:

https://files.brindlecove.net/share/folders/7qXk2mPz9LwRt4VhYs3NcB0aJdE6uFgHo?mode=viewer

```html
<!DOCTYPE html>
<html lang="en">
<head>
<meta charset="utf-8">
<title>Keystone Crew – Brochure Spread</title>
<link href="https://fonts.googleapis.com/css2?family=Archivo+Black&family=Archivo:wght@400;700;800&display=swap" rel="stylesheet">
<style>
  :root {
    --backdrop: #9d9d9d;
    --paper: #f2f2f3;
    --paper-shade: #dcdcde;
    --brand-red: #8b1a1d;
    --deep-red: #4a1214;
    --ink: #3f3f3f;
    --ink-soft: #555555;
    --photo-dark: #2e2e30;
    --photo-mid: #8a8b8d;
    --white: #ffffff;
  }
  * { margin: 0; padding: 0; box-sizing: border-box; }
  html, body { width: 1200px; height: 1000px; overflow: hidden; }
  body { background: var(--backdrop); font-family: "Archivo", Arial, sans-serif; position: relative; }

  .page {
    position: absolute; top: 78px; width: 594px; height: 842px; overflow: hidden;
    background: linear-gradient(150deg, var(--paper-shade) 0%, var(--paper) 35%, #e6e6e8 60%, var(--paper) 100%);
  }
  .page--left { left: 3px; }
  .page--right { left: 603px; }
  .page svg.shapes { position: absolute; inset: 0; }

  .page-number { position: absolute; bottom: 16px; right: 24px; font-size: 13px; color: #777; }

  /* Left page */
  .brand { position: absolute; left: 28px; top: 50px; display: flex; align-items: center; gap: 10px; }
  .brand__mark { width: 16px; height: 16px; background: var(--ink); }
  .brand__name { font-family: "Archivo", Arial, sans-serif; font-weight: 800; font-size: 30px; color: var(--brand-red); letter-spacing: -0.5px; }

  .tagline {
    position: absolute; right: 37px; top: 36px; width: 240px; text-align: right;
    font-family: "Archivo", Arial, sans-serif; font-weight: 800; font-size: 17px; line-height: 22px;
    color: var(--white); letter-spacing: 0.6px; text-transform: uppercase;
  }
  .intro {
    position: absolute; left: 38px; top: 158px; width: 272px;
    font-size: 14px; line-height: 19.5px; color: var(--ink-soft);
  }
  .intro strong { color: var(--ink); }
  .motto {
    position: absolute; left: 47px; top: 310px;
    font-family: "Archivo Black", "Arial Black", sans-serif; font-size: 36px; line-height: 48px;
    color: var(--brand-red); letter-spacing: 1.5px; text-transform: uppercase;
  }
  .values-lead {
    position: absolute; right: 37px; top: 489px; width: 260px; text-align: right;
    font-size: 14px; line-height: 19.5px; color: var(--ink-soft);
  }

  /* Right page */
  .side-title {
    position: absolute; left: 40px; top: 285px; transform-origin: left top; transform: rotate(-90deg);
    font-family: "Archivo Black", "Arial Black", sans-serif; font-size: 46px; letter-spacing: 4px;
    color: var(--white); white-space: nowrap;
  }
  .section-title { position: absolute; left: 128px; top: 62px; text-transform: uppercase; }
  .section-title__small { display: block; font-family: "Archivo Black", "Arial Black", sans-serif; font-size: 30px; line-height: 32px; color: var(--ink); letter-spacing: 1px; }
  .section-title__large { display: block; font-family: "Archivo Black", "Arial Black", sans-serif; font-size: 52px; line-height: 56px; color: var(--brand-red); letter-spacing: 1px; }

  .team-icon { position: absolute; left: 448px; top: 28px; width: 92px; height: 100px; }

  .steps { position: absolute; left: 120px; top: 174px; width: 400px; list-style: none; }
  .step { position: relative; height: 127px; }
  .step__heading {
    text-align: right; width: 267px; margin-left: 0; font-weight: 800; font-size: 12.5px;
    letter-spacing: 0.8px; color: var(--ink); text-transform: uppercase; margin-bottom: 9px; padding-right: 0;
  }
  .step__text { width: 267px; text-align: right; font-size: 11.5px; line-height: 14.3px; color: var(--ink-soft); }
  .step__number {
    position: absolute; left: 330px; top: -6px; width: 80px; text-align: center;
    font-family: "Archivo Black", "Arial Black", sans-serif; font-size: 64px; line-height: 70px; color: var(--brand-red);
  }
</style>
</head>
<body>

  <section class="page page--left">
    <svg class="shapes" width="594" height="842" viewBox="0 0 594 842">
      <defs>
        <linearGradient id="bandRed" x1="0" y1="0" x2="1" y2="1">
          <stop offset="0" stop-color="#5a1619"/>
          <stop offset="1" stop-color="#3a0e10"/>
        </linearGradient>
        <linearGradient id="siteTonesLeft" x1="0" y1="0" x2="1" y2="1">
          <stop offset="0" stop-color="#4a4b4e"/>
          <stop offset="0.5" stop-color="#2a2a2c"/>
          <stop offset="1" stop-color="#6d6e70"/>
        </linearGradient>
      </defs>
      <polygon class="header-band" points="190,0 594,0 594,312" fill="url(#bandRed)"/>
      <polygon points="0,455 494,842 0,842" fill="url(#siteTonesLeft)" role="img" aria-label="Black and white photo of steel beams hanging from a crane on a construction site"/>
      <polygon points="494,842 594,762 594,842" fill="#fafafa"/>
    </svg>

    <div class="brand">
      <span class="brand__mark"></span>
      <span class="brand__name">Keystone Crew</span>
    </div>

    <h2 class="tagline">Industry leading recruitment &amp; labour hire agency in New South Wales</h2>

    <p class="intro">At <strong>Keystone Crew</strong>, we're all about ensuring our clients achieve their goals and succeed in their field. This is why so many construction companies have trusted us in providing qualified workers for their projects. Make an enquiry and watch these words be put into action.</p>

    <h1 class="motto">Inspiring others.<br>Achieving goals.<br>Working to succeed.</h1>

    <p class="values-lead">We are extremely passionate about what we do, excellence in the Labour Hire industry has become second nature for us. We work to give you many reasons to engage with Keystone Crew services. We have become a well renowned Recruitment &amp; Labour Hire company by upholding the following values:</p>

    <span class="page-number">1</span>
  </section>

  <section class="page page--right">
    <svg class="shapes" width="594" height="842" viewBox="0 0 594 842">
      <defs>
        <linearGradient id="siteTonesRight" x1="0" y1="0" x2="1" y2="1">
          <stop offset="0" stop-color="#5b5c5f"/>
          <stop offset="0.45" stop-color="#b9babc"/>
          <stop offset="1" stop-color="#7c7d80"/>
        </linearGradient>
      </defs>
      <polygon points="0,470 497,842 0,842" fill="url(#siteTonesRight)" role="img" aria-label="Black and white photo of a worker climbing a steel frame structure on site"/>
      <polygon points="497,842 594,762 594,842" fill="#fafafa"/>
      <line class="progress-arrow" x1="495" y1="838" x2="495" y2="628" stroke="var(--brand-red)" stroke-width="1.5"/>
      <polygon points="481,638 495,612 509,638" fill="var(--brand-red)"/>
    </svg>

    <div class="side-title">WHY US?</div>

    <h2 class="section-title">
      <span class="section-title__small">Our</span>
      <span class="section-title__large">Process</span>
    </h2>

    <svg class="team-icon" viewBox="0 0 92 100" aria-hidden="true">
      <g fill="var(--brand-red)">
        <circle cx="46" cy="8" r="7"/>
        <path d="M36 28 q0-10 10-10 q10 0 10 10 z"/>
        <path d="M8 50 v-14 h76 v14" fill="none" stroke="var(--brand-red)" stroke-width="4"/>
        <rect x="44" y="28" width="4" height="10"/>
        <g>
          <circle cx="13" cy="58" r="5"/><rect x="7" y="65" width="12" height="20" rx="3"/><rect x="8" y="84" width="4" height="14"/><rect x="14" y="84" width="4" height="14"/>
          <circle cx="35" cy="58" r="5"/><rect x="29" y="65" width="12" height="20" rx="3"/><rect x="30" y="84" width="4" height="14"/><rect x="36" y="84" width="4" height="14"/>
          <circle cx="57" cy="58" r="5"/><rect x="51" y="65" width="12" height="20" rx="3"/><rect x="52" y="84" width="4" height="14"/><rect x="58" y="84" width="4" height="14"/>
          <circle cx="79" cy="58" r="5"/><rect x="73" y="65" width="12" height="20" rx="3"/><rect x="74" y="84" width="4" height="14"/><rect x="80" y="84" width="4" height="14"/>
        </g>
      </g>
    </svg>

    <ol class="steps">
      <li class="step">
        <h3 class="step__heading">Initiation</h3>
        <p class="step__text">Keystone Crew initially engages with the employer to create a business relationship. We understand the clients' needs and assign appropriate measures to forward our services.</p>
        <span class="step__number">1</span>
      </li>
      <li class="step">
        <h3 class="step__heading">Assessment</h3>
        <p class="step__text">We assess the employers' criteria and hand over the appropriate candidates for their job. Unlike most recruitment companies, we do not bulk-send a bunch of resumes, but rather ensure that we are sending the greatest quality candidates that best meet their needs.</p>
        <span class="step__number">2</span>
      </li>
      <li class="step">
        <h3 class="step__heading">Placement</h3>
        <p class="step__text">Employers then interview the candidate put forward by Keystone Crew in order to fill the vacancy and ensure that the candidate is the best fit for their position.</p>
        <span class="step__number">3</span>
      </li>
    </ol>

    <span class="page-number">2</span>
  </section>

</body>
</html>
```